Tri-Fold Flyer for Life Coaching Business

We require a tri-fold DL flyer for our Life Coaching business, Tall Harbor.
The flyer needs to be bold, engaging and professional with broad appeal. Ideally it will include a few images and/or graphics, but shouldn’t be too busy.
As a generalist life coaching business, image selection needs to be broad enough to attract clients who are interested in Career, Relationship or General Life Coaching (think Health, Wealth & Balance). Please feel free to use any images/graphics you think are suitable. We have also purchased a selection of images from PixVault that you may wish to use - these can be viewed on our website www.tallharbor-example.com - originals can be requested.
Unlike a lot of coaching businesses, we are not interested in being too cheesy, flowery or spiritual. Our style is direct, up-front and to the point - we don’t take ourselves too seriously. The flyer should reflect this.
Attached is a basic template that shows the required text and an example of layout - however we are very flexible with the layout/design, so please don’t be limited by this (eg. Image on the front is only used as a placeholder, testimonials may work better somewhere else etc).
Also attached is a copy of our business card and logo. This will give you an idea of the designs that we are already using. Again, this is as a guide only - however we would definitely like to use similar fonts to the business card (Helvetica or Helvetica Neue I think) and have the blue from the logo incorporated. It would be great to see icons (similar to what has been used on the business card) for phone number, email address etc. Different versions of the logo (format, colour etc) are available.
Aside from this we would like you to use your creative flair and show us different versions of the flyer. Thank You and Good Luck!
Updates
Hi everyone,
Industry/Entity Type
Life Coaching
Requirements
Must have
- Brochure should be tri-fold DL
Logo should be included - preferably on back cover
Contact details and call to action should be prominent/obvious

```html
<!DOCTYPE html>
<html lang="en">
<head>
<meta charset="utf-8">
<title>Tall Harbor – Tri-Fold Flyer</title>
<link href="https://fonts.googleapis.com/css2?family=Questrial&family=Didact+Gothic&display=swap" rel="stylesheet">
<style>
  :root{
    --backdrop:#2a2a2a;
    --cream-light:#fcf4d2;
    --cream:#f5e6a8;
    --cream-deep:#e8d384;
    --sand:#d9c48a;
    --sand-dark:#c7b27a;
    --blue:#1b9ad6;
    --blue-dark:#0f7fbf;
    --brown:#7a4e22;
    --orange:#c27a2c;
    --text:#4a3a22;
    --white:#ffffff;
  }
  *{box-sizing:border-box;margin:0;padding:0}
  html,body{width:1200px;height:901px;overflow:hidden}
  body{background:var(--backdrop);font-family:"Didact Gothic","Questrial",sans-serif;color:var(--text);position:relative}
  .spread{position:absolute;left:313px;width:576px;height:375px;display:flex;box-shadow:0 2px 8px rgba(0,0,0,.5)}
  .spread--outside{top:53px}
  .spread--inside{top:466px}
  .panel{position:relative;width:192px;height:100%;overflow:hidden;
    background:linear-gradient(180deg,var(--cream-light) 0%,var(--cream) 100%)}
  .panel + .panel{border-left:1px solid rgba(160,130,60,.25)}
  .photo{position:absolute;display:block}
  .abs{position:absolute}
  p{font-size:5.8px;line-height:1.45}

  /* outside: panel 1 */
  .group-photo{left:28px;top:24px;width:122px;height:70px;border-radius:4px;
    background:linear-gradient(160deg,#b9b6ad,#5b5448 60%,#2c2a2a);border:2px solid var(--white)}
  .pin{position:absolute;width:9px;height:9px;border-radius:50%;background:var(--sand-dark);border:1.5px solid var(--white)}
  .rut-box{left:0;top:140px;width:192px;height:160px;background:var(--sand);border-radius:50% 50% 0 0/22px 22px 0 0;
    padding:46px 20px 0;text-align:center}
  .rut-title{font-family:"Questrial",sans-serif;font-size:8px;line-height:1.35;color:var(--text)}
  .rut-rule{height:1px;background:rgba(90,70,30,.35);margin:6px 0}
  .rut-q{font-size:5.8px;line-height:1.4}
  .mountain-photo{left:0;top:300px;width:192px;height:75px;
    background:linear-gradient(180deg,#3c7ec7 0%,#8cb8e0 55%,#e9eef2 72%,#6c6a70 100%)}
  .mountain-text{left:74px;top:318px;color:var(--white);font-family:"Questrial",sans-serif;font-size:6.5px;line-height:1.3}
  .mountain-text strong{font-size:9px;font-weight:400;color:#ffe27a}

  /* outside: panel 2 */
  .meeting-photo{left:30px;top:6px;width:150px;height:80px;border-radius:0 0 40px 40px;
    background:linear-gradient(150deg,#e8e6e2,#a8a39a 55%,#3d3a38)}
  .intro-box{left:0;top:110px;width:192px;height:104px;background:var(--sand);padding:22px 20px 0;text-align:center}
  .intro-box p{font-size:5.8px;line-height:1.75}
  .cta{left:16px;top:222px;width:160px;text-align:center;font-size:6.6px;line-height:1.6}
  .name{font-family:"Questrial",sans-serif;font-weight:400;color:var(--blue);white-space:nowrap}
  .name--small{left:0;width:192px;top:262px;text-align:center;font-size:9px}
  .contacts{left:0;top:288px;width:192px;text-align:center;font-size:7.4px;line-height:2.05;color:var(--brown)}
  .abn{right:8px;bottom:5px;font-size:3.8px;color:var(--text)}

  /* outside: panel 3 */
  .cover-photo{left:0;top:0;width:192px;height:178px;
    background:linear-gradient(170deg,#eef0f2 0%,#c9c6c2 40%,#6e5b50 70%,#2d2b30 100%)}
  .cover-swoosh{left:0;top:130px;width:192px;height:70px}
  .name--cover{left:0;width:192px;top:188px;text-align:center;font-size:19px}
  .tagline{left:0;top:226px;width:192px;text-align:center;color:var(--blue);font-family:"Questrial",sans-serif}
  .tagline-1{font-size:10px}
  .tagline-2{font-size:15px;letter-spacing:.3px;margin-top:5px}
  .name--footer{left:0;width:192px;top:304px;text-align:center;font-size:8.5px}
  .services-bar{left:0;top:340px;width:192px;height:16px;background:var(--blue);color:var(--white);
    font-size:6.4px;display:flex;align-items:center;justify-content:center}

  /* inside */
  h2{font-family:"Questrial",sans-serif;font-weight:400;color:var(--brown)}
  .inner-1 h2{position:absolute;left:14px;top:24px;font-size:10px}
  .copy{position:absolute;left:14px;width:166px}
  .copy p{margin-bottom:7px}
  .inner-1 .copy p{font-size:6.4px;text-align:justify;margin-bottom:8px}
  .inner-2 .copy p{font-size:6.1px;text-align:justify}
  .office-photo{left:0;top:298px;width:192px;height:77px;
    background:linear-gradient(160deg,#f0efec,#b2aca4 50%,#3d3937)}
  .curve{position:absolute;left:0;width:192px}
  .hero-photo{left:0;top:0;width:192px;height:80px;
    background:linear-gradient(170deg,#f1f1f1,#9a9aa0 50%,#2e2f36)}
  .inner-2 h2{position:absolute;left:20px;top:103px;font-size:16px}
  .list-title{left:18px;top:262px;font-size:6.3px;color:var(--orange)}
  .issues{position:absolute;left:18px;top:274px;list-style:none;font-size:5px;line-height:1.85}
  .issues li::before{content:"";display:inline-block;width:4px;height:4px;border-radius:50%;
    background:var(--cream-deep);border:1px solid var(--orange);margin-right:6px;vertical-align:-0.5px}
  .inner-3 h2{font-size:9px}
  .h-work{left:10px;top:10px}
  .career-photo{left:120px;top:12px;width:62px;height:70px;border-radius:3px;
    background:linear-gradient(160deg,#3d6fa5,#1f3a5c 60%,#0f1d30)}
  .h-get{left:10px;top:182px}
  .quote{font-style:italic}
  .sign{text-align:right;font-size:4.8px;margin-top:-4px}
</style>
</head>
<body>

<section class="spread spread--outside">
  <div class="panel">
    <div class="photo group-photo" role="img" aria-label="Photo of a cheerful business team celebrating"></div>
    <span class="pin" style="left:22px;top:18px"></span>
    <span class="pin" style="left:144px;top:18px"></span>
    <span class="pin" style="left:22px;top:88px"></span>
    <div class="abs rut-box">
      <div class="rut-title">Are you stuck in a rut or<br>at a crossroads in life?</div>
      <div class="rut-rule"></div>
      <div class="rut-q">Do you have ongoing problems with your career, relationship or just life itself?</div>
      <div class="rut-rule"></div>
      <div class="rut-q">Would you like to change your direction, or regain some clarity in life?</div>
    </div>
    <div class="photo mountain-photo" role="img" aria-label="Photo of a woman raising her arms on a mountain top"></div>
    <div class="abs mountain-text">Let us help you to create<br><strong>your very own Tall Harbor!</strong></div>
  </div>

  <div class="panel">
    <div class="photo meeting-photo" role="img" aria-label="Photo of a coach in conversation with a client"></div>
    <svg class="abs" style="left:30px;top:60px" width="150" height="32" viewBox="0 0 150 32" aria-hidden="true">
      <path d="M0 0 Q10 30 75 28 Q135 26 150 0 L150 6 Q138 32 75 32 Q8 32 0 6Z" fill="var(--blue)"/>
    </svg>
    <div class="abs intro-box">
      <p>Tall Harbor is a professional coaching service that helps people like you achieve the outcomes that you're looking for. It doesn't matter what the challenge is, coaching can take you from where you are now, to where you want to be.</p>
    </div>
    <div class="abs cta">Call now for a free introductory session or visit our website to download our e-book!</div>
    <div class="abs name name--small">Tall Harbor</div>
    <div class="abs contacts">
      Phone : (03) 9555 0142<br>
      Email : info@tallharbor-example.com<br>
      Visit us at : www.tallharbor-example.com
    </div>
    <div class="abs abn">ABN: 00 000 000 000</div>
  </div>

  <div class="panel">
    <div class="photo cover-photo" role="img" aria-label="Photo of a confident businesswoman in an office"></div>
    <svg class="abs cover-swoosh" viewBox="0 0 192 70" preserveAspectRatio="none" aria-hidden="true">
      <path d="M0 70 L0 48 Q96 10 192 30 L192 70Z" fill="var(--cream-light)"/>
      <path d="M0 48 Q96 10 192 30 L192 36 Q96 18 0 54Z" fill="var(--sand-dark)"/>
    </svg>
    <div class="abs name name--cover">Tall Harbor</div>
    <div class="abs tagline">
      <div class="tagline-1">Take control of your life</div>
      <div class="tagline-2">RIGHT NOW!</div>
    </div>
    <div class="abs name name--footer">Tall Harbor</div>
    <div class="abs services-bar">Career | Relationship | Life Coaching</div>
  </div>
</section>

<section class="spread spread--inside">
  <div class="panel inner-1">
    <h2>What is coaching all about?</h2>
    <div class="copy" style="top:48px">
      <p>Life coaching is one of the leading tools that successful people use to live extraordinary lives. A conversation like no other, coaching will help you to regain clarity and direction in life, and unlock your ability to reach your full potential.</p>
      <p>We use proven processes that can take you from where you are now to where you want to be. All it takes is commitment and a willingness to learn to achieve the results you really want!</p>
      <p>During a coaching session you will discover ways to overcome barriers and limiting beliefs, you will learn how to achieve more in life, set meaningful goals and live life according to your rules.</p>
      <p>There is absolutely no reason for you to remain stuck in the situation you're in when we can help you to achieve the future that you always dreamed of.</p>
    </div>
    <svg class="curve" style="top:282px" height="30" viewBox="0 0 192 30" preserveAspectRatio="none" aria-hidden="true">
      <path d="M0 30 Q60 0 192 18 L192 24 Q60 8 0 30Z" fill="var(--blue)"/>
    </svg>
    <div class="photo office-photo" style="clip-path:path('M0 20 Q60 2 192 22 L192 77 L0 77Z')" role="img" aria-label="Photo of colleagues in a business meeting"></div>
  </div>

  <div class="panel inner-2">
    <div class="photo hero-photo" role="img" aria-label="Photo of a businessman reaching toward a glowing interface"></div>
    <svg class="curve" style="top:58px" height="40" viewBox="0 0 192 40" preserveAspectRatio="none" aria-hidden="true">
      <path d="M0 22 Q96 50 192 10 L192 40 L0 40Z" fill="var(--cream-light)"/>
      <path d="M0 18 Q96 48 192 6 L192 14 Q96 52 0 26Z" fill="var(--blue)"/>
    </svg>
    <h2>Who is it for?</h2>
    <div class="copy" style="top:128px;left:20px;width:160px">
      <p>At some stage in our lives, many of us hit a roadblock or get to a point where we feel like we've lost our direction or our sense of purpose. This can show up in many ways, but some common symptoms are procrastination, self sabotage, or a lack of self belief. This can affect our self esteem and the relationships with the people that we care about the most. Even more than this, it can dramatically influence how we experience life in general.</p>
      <p>Coaching is for anyone who wants to make changes in their life. You may want to address a particular challenge, or you may just be ready to take life to the next level.</p>
    </div>
    <div class="abs list-title">Coaching can assist with issues such as</div>
    <ul class="issues">
      <li>Achieving life balance</li>
      <li>Relationship issues</li>
      <li>Career &amp; Business planning</li>
      <li>Managing stress</li>
      <li>Losing weight</li>
      <li>Boosting self confidence</li>
      <li>Overcoming negative emotions &amp; patterns</li>
      <li>Getting organised &amp; managing time effectively</li>
    </ul>
  </div>

  <div class="panel inner-3">
    <h2 class="abs h-work">How does it work?</h2>
    <div class="photo career-photo" role="img" aria-label="Photo of a hand pointing at career and skills keywords"></div>
    <div class="copy" style="top:23px;left:10px;width:104px">
      <p>Coaching is usually conducted over a series of sessions lasting from 45 minutes to one hour. Sessions can be conducted face-to-face, or over the phone depending on your location and preference. How many sessions you need depends on what you want to achieve.</p>
    </div>
    <div class="copy" style="top:118px;left:10px;width:172px">
      <p>We know that no two people are the same - each person has different needs and likes a different approach - so before we actually start, we offer you a free introductory session.</p>
      <p>During this session we will look at whether coaching would be beneficial for you and how it can help you to make changes in your life.</p>
    </div>
    <h2 class="abs h-get">What will you get out of it?</h2>
    <div class="copy" style="top:194px;left:10px;width:172px">
      <p>Our programs are designed to help you achieve clarity and awareness that will assist you in making decisions that will ultimately lead you to your desired outcomes. We'll share valuable strategies and tools that will help you to make the changes that are needed in your life.</p>
      <p>During our sessions you'll learn how to overcome your fears, how to deal with your emotions and thoughts, how to set goals that have meaning for you and how you can live your life in true alignment with your values.</p>
      <p class="quote">"There has been laughter, tears, frustration, joy, exhilaration, and light bulb moments in every session I have had. If anyone is even considering taking this journey, please for your own sake do it... you will never look back."</p>
      <p class="sign">Dana R</p>
      <p class="quote">"Their positivity and encouragement really helped me to keep motivated and focused. I found them to be very caring and genuinely interested in helping me realise my strengths and potential."</p>
      <p class="sign">Mel K</p>
    </div>
  </div>
</section>

</body>
</html>
```